Flyer Design Project

We need a flyer design for our company based in Ontario, Canada called CrateNest. We rent out plastic reusable moving boxes. Please visit Cratenest.ca to find out more information about our company. We are looking for a creative, clean, and fun flyer design. The flyers purpose is to share with others what services CrateNest offers as well as how convient our service is while still being cheaper than cardboard boxes.

Industry/Entity Type

Plastic

```html
<!DOCTYPE html>
<html lang="en">
<head>
<meta charset="utf-8">
<title>CrateNest – Plastic Moving Boxes Flyer</title>
<link rel="stylesheet" href="https://fonts.googleapis.com/css2?family=Inter:wght@300;400;600;700;800;900&family=Oswald:wght@500;600&display=swap">
<style>
  :root {
    --green: #76ec00;
    --green-band: #7cf300;
    --green-deep: #5fc800;
    --ink: #0b0b0b;
    --grey: #5a5a5a;
    --badge: #4a4a4a;
    --white: #ffffff;
  }
  * { box-sizing: border-box; margin: 0; padding: 0; }
  html, body { width: 927px; height: 1200px; overflow: hidden; background: var(--white); }
  .flyer {
    position: relative; width: 927px; height: 1200px; overflow: hidden;
    background: var(--white); font-family: "Inter", Arial, sans-serif; color: var(--ink);
  }
  .site-url {
    position: absolute; top: 24px; right: 36px;
    font-size: 20px; font-weight: 700; color: var(--green);
  }
  .tagline {
    position: absolute; left: 68px; top: 86px;
    font-size: 35px; font-weight: 700; letter-spacing: -0.3px;
  }
  .headline {
    position: absolute; left: 64px; top: 118px;
    font-size: 104px; font-weight: 300; letter-spacing: -2px; line-height: 1.1;
  }
  .steps { position: absolute; left: 72px; top: 290px; width: 300px; }
  .step { position: absolute; left: 0; width: 300px; }
  .step-label { font-size: 14px; font-weight: 700; color: var(--grey); }
  .step-body { display: flex; gap: 12px; margin-top: 6px; }
  .step-icon {
    flex: none; width: 76px; height: 74px; border-radius: 8px;
    background: var(--green); display: flex; align-items: center; justify-content: center;
  }
  .step-text { font-size: 16px; font-weight: 700; line-height: 20.5px; margin-top: -2px; }
  .product-visual {
    position: absolute; left: 360px; top: 280px; width: 510px; height: 360px;
    background: linear-gradient(160deg, #9bff2a 0%, #7fe80a 55%, #5cbf00 100%);
    border-radius: 6px;
  }
  .reasons-band {
    position: absolute; left: 0; top: 677px; width: 927px; height: 376px;
    background: var(--green-band); color: var(--white);
  }
  .order-badge {
    position: absolute; left: 706px; top: 598px; width: 184px; height: 184px;
    border-radius: 50%; background: var(--badge); border: 7px solid var(--white);
    display: flex; align-items: center; justify-content: center; text-align: center;
    font-family: "Oswald", "Arial Narrow", sans-serif; font-weight: 600;
    font-size: 44px; line-height: 48px; color: var(--white);
  }
  .why-title { position: absolute; left: 64px; top: 30px; font-size: 30px; font-weight: 900; }
  .why-sub { position: absolute; left: 64px; top: 74px; font-size: 25px; font-weight: 600; }
  .why-copy {
    position: absolute; left: 64px; top: 118px; width: 428px;
    font-size: 15px; font-weight: 700; line-height: 20.8px;
  }
  .reason-list { position: absolute; left: 524px; top: 86px; list-style: none; }
  .reason { display: flex; align-items: center; height: 52px; }
  .reason-num {
    width: 36px; height: 36px; background: var(--white); color: var(--green-band);
    font-weight: 900; font-size: 28px; display: flex; align-items: center; justify-content: center;
  }
  .reason-name {
    margin-left: 14px; font-family: "Oswald", "Arial Narrow", sans-serif;
    font-weight: 500; font-size: 26px; letter-spacing: 0.2px;
  }
  .contact { position: absolute; left: 68px; top: 1080px; }
  .contact-lead { font-size: 22px; font-weight: 700; color: var(--grey); }
  .contact-phone {
    display: flex; align-items: center; gap: 4px; margin-top: 6px; margin-left: -14px;
    font-size: 45px; font-weight: 800; color: var(--green); letter-spacing: -0.5px;
  }
  .brand { position: absolute; right: 46px; top: 1094px; display: flex; align-items: center; gap: 12px; }
  .brand-mark { width: 54px; height: 54px; background: var(--green); }
  .brand-name { font-size: 34px; font-weight: 900; color: var(--ink); letter-spacing: -0.5px; }
</style>
</head>
<body>
<main class="flyer">
  <p class="site-url">www.cratenest.ca</p>
  <h2 class="tagline">Plastic, stackable, eco-friendly</h2>
  <h1 class="headline">moving boxes</h1>

  <section class="steps">
    <div class="step" style="top:0">
      <p class="step-label">Step : 1</p>
      <div class="step-body">
        <div class="step-icon">
          <svg width="52" height="36" viewBox="0 0 52 36" aria-hidden="true">
            <rect x="2" y="2" width="30" height="24" fill="#fff"/>
            <path d="M34 10h9l7 8v8H34z" fill="#fff"/>
            <circle cx="12" cy="29" r="5" fill="#fff" stroke="#76ec00" stroke-width="2"/>
            <circle cx="41" cy="29" r="5" fill="#fff" stroke="#76ec00" stroke-width="2"/>
          </svg>
        </div>
        <p class="step-text">We deliver your moving boxes right to your front door (unless you prefer side door).</p>
      </div>
    </div>
    <div class="step" style="top:119px">
      <p class="step-label">Step : 2</p>
      <div class="step-body">
        <div class="step-icon">
          <svg width="48" height="44" viewBox="0 0 48 44" aria-hidden="true">
            <path d="M6 18h36v24H6z" fill="#fff"/>
            <path d="M6 18L1 8l20-4 3 14zM42 18l5-10-20-4-3 14z" fill="#fff"/>
          </svg>
        </div>
        <p class="step-text">Pack it up! Our boxes protect your belongings and make stacking safe.</p>
      </div>
    </div>
    <div class="step" style="top:238px">
      <p class="step-label">Step : 3</p>
      <div class="step-body">
        <div class="step-icon">
          <svg width="46" height="42" viewBox="0 0 46 42" aria-hidden="true">
            <path d="M23 2L2 20h6v20h11V28h8v12h11V20h6z" fill="#fff"/>
          </svg>
        </div>
        <p class="step-text">Once you're unpacked we'll come by your new home and collect the moving boxes.</p>
      </div>
    </div>
  </section>

  <div class="product-visual" role="img" aria-label="Bright green lidded plastic moving crate with the brand name on its side"></div>

  <section class="reasons-band">
    <h2 class="why-title">Why choose CrateNest?</h2>
    <h3 class="why-sub">We have 5 good reasons</h3>
    <p class="why-copy">Packing boxes is the same no matter how old you are, what race you are, where you’re moving to, or what your favorite ice cream is. Packing is packing, but are boxes, boxes? We all remember the search for cardboard boxes from family, friends and even local grocery stores. We get a few good ones, a few mediocre ones and a few banana boxes with a big hole in the bottom. “That’s fine for bedding, right?”. But at the end of the day, we still didn’t have enough quality boxes. When you order from CrateNest, we have an answer for all the box problems we used to run into:</p>
    <ol class="reason-list">
      <li class="reason"><span class="reason-num">1</span><span class="reason-name">WE DELIVER</span></li>
      <li class="reason"><span class="reason-num">2</span><span class="reason-name">PACK SECURELY</span></li>
      <li class="reason"><span class="reason-num">3</span><span class="reason-name">SAFELY STACK</span></li>
      <li class="reason"><span class="reason-num">4</span><span class="reason-name">WE PICKUP</span></li>
      <li class="reason"><span class="reason-num">5</span><span class="reason-name">ENVIRONMENTALLY FRIENDLY</span></li>
    </ol>
  </section>

  <div class="order-badge">ORDER<br>NOW</div>

  <section class="contact">
    <p class="contact-lead">Call us now with any questions</p>
    <p class="contact-phone">
      <svg width="16" height="34" viewBox="0 0 16 34" aria-hidden="true">
        <path d="M13 2H7C3 2 2 6 2 17s1 15 5 15h6v-8H9c-1-2-1-12 0-14h4z" fill="none" stroke="#76ec00" stroke-width="3" stroke-linejoin="round"/>
      </svg>
      1-800-555-0142
    </p>
  </section>

  <div class="brand">
    <span class="brand-mark"></span>
    <span class="brand-name">CRATENEST</span>
  </div>
</main>
</body>
</html>
```